Tom Verlane

I am the director of Casa Del Humo International. We make premium cigars

I want an insanely beautiful card that directly attracts attention. Do your best. The card can use emboss, foil, laser-cut metal or anything else. Make it stand out, but also elegant.

Target Market(s)

Cigar Distributors

Industry/Entity Type

Cigars

Contact Information for Business Card

Email: tom.verlane@verlanos.com + Logos (attached) + Position: Director + 'High-End Cigars'

Colors

Designer to choose colors to be used in the design.

Requirements
Nice to have
• Please check us out at www.casadelhumo.com and try to use our colors and styles

```html
<!DOCTYPE html>
<html lang="en">
<head>
<meta charset="utf-8">
<title>Casa del Humo International – Business Card</title>
<link rel="stylesheet" href="https://fonts.googleapis.com/css2?family=EB+Garamond:wght@400;500&family=Tinos:wght@400;700&family=Arimo:wght@400&display=swap">
<style>
  :root {
    --backdrop: #d4d4d4;
    --paper: #ffffff;
    --ink: #231f20;
    --card-dark: #231f20;
    --red: #c8252d;
    --grey-text: #5a5a5a;
    --gold: #b39a6a;
    --white: #ffffff;
  }
  * { margin: 0; padding: 0; box-sizing: border-box; }
  html, body {
    width: 965px; height: 1200px; overflow: hidden;
    background: var(--backdrop);
  }
  .card {
    position: absolute; left: 108px; width: 749px; height: 427px;
    box-shadow: 2px 3px 5px rgba(0,0,0,0.28);
  }
  .card--front { top: 148px; background: var(--paper); color: var(--ink); }
  .card--back  { top: 626px; background: var(--card-dark); color: var(--white); }

  .frame {
    position: absolute; left: 25px; top: 25px; right: 25px; bottom: 25px;
    border: 1.5px solid var(--red);
  }

  .company {
    position: absolute; left: 0; right: 0; text-align: center;
    font-family: "EB Garamond", serif; font-weight: 400;
    letter-spacing: 0.3px;
  }
  .card--front .company { top: 76px; font-size: 27px; }
  .card--back  .company { top: 115px; font-size: 30px; }

  .rule { position: absolute; height: 1.5px; background: var(--red); }
  .rule::after {
    content: ""; position: absolute; left: 50%; top: 50%;
    width: 9px; height: 9px; background: var(--red);
    transform: translate(-50%, -50%) rotate(45deg);
  }
  .card--front .rule { left: 144px; width: 460px; top: 124px; }
  .card--back  .rule { left: 124px; width: 501px; top: 170px; }

  .location {
    position: absolute; left: 0; right: 0; text-align: center;
    font-family: "Arimo", sans-serif;
  }
  .card--front .location { top: 146px; font-size: 17px; }
  .card--back  .location { top: 193px; font-size: 19px; }

  .person {
    position: absolute; right: 395px; top: 246px; text-align: right;
    font-family: "Tinos", serif;
  }
  .person__name { font-weight: 700; font-size: 25px; color: var(--red); line-height: 30px; letter-spacing: 0.3px; }
  .person__role { font-size: 20px; color: var(--grey-text); line-height: 28px; }

  .divider {
    position: absolute; left: 374px; top: 251px; width: 1.5px; height: 50px;
    background: var(--red);
  }

  .contacts {
    position: absolute; left: 393px; top: 247px; list-style: none;
    font-family: "Tinos", serif; font-size: 20px; color: var(--grey-text);
  }
  .contacts li { display: flex; align-items: center; height: 26px; }
  .contacts svg { width: 16px; height: 16px; margin-right: 5px; flex: none; }

  .tagline {
    position: absolute; left: 0; right: 0; top: 388px; text-align: center;
    font-family: "Tinos", serif; font-size: 20px; color: var(--grey-text);
  }
  .tagline span { background: var(--paper); padding: 0 8px; }

  .brands {
    position: absolute; left: 0; right: 0; top: 328px; height: 60px;
    font-family: "EB Garamond", serif; font-weight: 500;
  }
  .brand {
    position: absolute; top: 0; display: flex; align-items: center; height: 60px;
    transform: translateX(-50%); white-space: nowrap; font-size: 27px;
  }
  .brand--castellan { left: 208px; color: var(--red); }
  .brand--vantoria  { left: 368px; color: var(--gold); }
  .brand--almadena  { left: 531px; color: var(--white); }
</style>
</head>
<body>

<section class="card card--front" aria-label="Card front">
  <div class="frame"></div>
  <h1 class="company">CASA del HUMO INTERNATIONAL</h1>
  <div class="rule"></div>
  <p class="location">ORVANA - CASTELIA</p>

  <div class="person">
    <p class="person__name">TOM VERLANE</p>
    <p class="person__role">Director</p>
  </div>
  <div class="divider"></div>
  <ul class="contacts">
    <li>
      <svg viewBox="0 0 16 16" aria-hidden="true">
        <path d="M1 6 L8 1.5 L15 6 V14.5 H1 Z" fill="#c8252d"/>
        <path d="M1 6 L8 10.5 L15 6" fill="none" stroke="#fff" stroke-width="1.1"/>
      </svg>
      tom.verlane@verlanos.com
    </li>
    <li>
      <svg viewBox="0 0 16 16" aria-hidden="true">
        <circle cx="8" cy="8" r="7" fill="#c8252d"/>
        <ellipse cx="8" cy="8" rx="3" ry="7" fill="none" stroke="#fff" stroke-width="1"/>
        <path d="M1 8 H15" stroke="#fff" stroke-width="1"/>
      </svg>
      www.casadelhumo.com
    </li>
  </ul>

  <p class="tagline"><span>High-End Cigars</span></p>
</section>

<section class="card card--back" aria-label="Card back">
  <div class="frame"></div>
  <h2 class="company">CASA del HUMO INTERNATIONAL</h2>
  <div class="rule"></div>
  <p class="location">ORVANA - CASTELIA</p>

  <div class="brands">
    <p class="brand brand--castellan">Castellan</p>
    <p class="brand brand--vantoria">Vantoria</p>
    <p class="brand brand--almadena">Almadena</p>
  </div>
</section>

</body>
</html>
```